B2B flyer solution for charging infrastructures (One-Pager Din A4, double-sided)

We need a professional design for our flyer in format Din A4/both sides.
Attached you will find the content for the flyer, but we are looking for a modern, professional design.

Some background/context information:
- the product is about a solution for charging and billing of charging infrastructures (for electric cars) in companies
- target group: companies, esp. facility managers, fleet managers, controlling, CTO, CEO
- should be printed and available online
- our website (and most of our current design work): https://vornix-tech.de

In the files you will find:
- photos of reference implementations of our solution (should be included in the flyer)
- stock photos (we are using the one you will find in the current flyer on our presentations, maybe you can use it too to keep some corporate identity.
- our logo
- the current flyer as PDF and as PowerPoint
- a sample presentation we also need for customer communication

It would be nice if the design will align with the existing design work, but bring fresh aspects and will be up-to-date and professional.

Target Market(s)

B2B, companies, fleet managers, facility managers, CTO, CIO

Industry/Entity Type

Enterprises, Charging Solutions for Electric Vehicles

Requirements
Nice to have
• Bright, light design, clean, readable

```html
<!DOCTYPE html>
<html lang="de">
<head>
<meta charset="utf-8">
<title>vornix-tech Professional – Flyer</title>
<link rel="stylesheet" href="https://fonts.googleapis.com/css2?family=Bebas+Neue&family=Montserrat:wght@400;500;600;700&display=swap">
<style>
:root{
  --stage:#d4d5d8;
  --paper:#ffffff;
  --ink:#111114;
  --panel:#0c0c10;
  --pink:#e0359a;
  --purple:#7a62b8;
  --band:linear-gradient(90deg,#e0359a 0%,#b655a8 55%,#7a62b8 100%);
  --white:#ffffff;
}
*{box-sizing:border-box;margin:0;padding:0}
html,body{width:1200px;height:829px;overflow:hidden}
body{background:var(--stage);font-family:"Montserrat",sans-serif;color:var(--ink);position:relative}
.page{position:absolute;top:58px;width:484px;height:684px;background:var(--paper);overflow:hidden}
.page--front{left:71px}
.page--back{left:645px}
.abs{position:absolute}
.brand{position:absolute;left:16px;top:80px;font-weight:600;font-size:25px;letter-spacing:-.3px;color:var(--ink)}
.band{position:absolute;left:0;width:100%;background:var(--band)}
.title{position:absolute;left:18px;font-family:"Bebas Neue",sans-serif;font-weight:400;color:var(--white);letter-spacing:.3px;white-space:nowrap}
.band-sub{position:absolute;left:18px;color:var(--white);font-weight:600;font-size:10px;line-height:12px}
.photo{position:absolute}
.intro{position:absolute;left:18px;top:291px;width:262px;font-weight:600;font-size:10.2px;line-height:12.2px}
.intro p+p{margin-top:12px}
.panel{position:absolute;background:var(--panel);color:var(--white)}
.panel h3{color:var(--pink);font-weight:700}
.dot-list{list-style:none}
.dot-list li{position:relative;padding-left:16px}
.dot-list li::before{content:"";position:absolute;left:1px;top:3px;width:6px;height:6px;border-radius:50%;border:1.3px solid var(--pink)}
.thumb{position:absolute;border:3px solid #d8459f}
.contact h4{color:var(--pink);font-weight:700;font-size:12px;margin-bottom:4px}
.contact p{font-size:8.8px;line-height:10.4px}
.feature{position:absolute;top:275px;width:110px;text-align:center}
.feature .icon-box{width:73px;height:73px;margin:0 auto;border-radius:4px;border:2px solid transparent;background:linear-gradient(#fff,#fff) padding-box,var(--band) border-box;display:flex;align-items:center;justify-content:center}
.feature span{display:block;margin-top:8px;font-weight:600;font-size:12.5px;line-height:12.5px}
.section-head{position:absolute;left:19px;top:393px;color:var(--pink);font-weight:700;font-size:15px}
.detail h3{font-size:12px;margin-bottom:4px}
.detail p,.detail li{font-size:8.2px;line-height:12.4px}
.detail ul{list-style:none}
.detail li::before{content:"· "}
.detail .indent{padding-left:6px}
</style>
</head>
<body>

<section class="page page--front">
  <div class="brand">vornix-tech.de</div>

  <div class="band" style="top:125px;height:157px"></div>
  <h1 class="title" style="top:140px;font-size:50px;line-height:46px">VORNIX-TECH<br>PROFESSIONAL</h1>
  <p class="band-sub" style="top:243px">die maßgeschneiderte B2B<br>Abrechnungslösung für Elektromobilität</p>

  <div class="photo" role="img" aria-label="Schnellladesäule in Weiß und Schwarz mit zwei Ladekabeln und kleiner Ladestele"
       style="left:284px;top:30px;width:196px;height:344px;border-radius:6px;background:linear-gradient(180deg,#f4f4f6 0%,#e6e6ea 60%,#cfd0d4 100%)"></div>

  <div class="intro">
    <p>Lade-Infrastruktur-Abrechnungslösungen für<br>Unternehmen, damit Lade-Infrastruktur<br>Erträge statt Kosten produziert.</p>
    <p>So wird Lade-Infrastruktur von einer Kostenstelle<br>zu einem Profitcenter.</p>
  </div>

  <div class="panel" style="left:0;top:377px;width:303px;height:221px;padding:10px 6px 0 21px">
    <h3 style="font-size:12.5px;margin-bottom:7px">Leistungen:</h3>
    <ul class="dot-list" style="font-size:8.9px;line-height:10.2px">
      <li style="margin-bottom:2px">Vielseitige Abrechnungsmöglichkeiten für<br>Fuhrpark, Mitarbeiter, Partnerunternehmen,<br>Mieter, Kunden und andere.</li>
      <li style="margin-bottom:2px">Full-Service-Betreuung (Monitoring,<br>Abrechnung, Benutzerbetreuung)</li>
      <li style="margin-bottom:2px">Integration in ihre Unternehmensabläufe</li>
      <li>Berücksichtigung von Eigentümer/Mieter-Konstellationen</li>
    </ul>
    <h3 style="font-size:12.5px;margin:13px 0 7px">Mit vornix-tech Professional profitieren:</h3>
    <ul class="dot-list" style="font-size:8.9px;line-height:10.2px">
      <li style="margin-bottom:3px">· Effizienter Verwaltung von Lade-Infrastruktur</li>
      <li style="margin-bottom:3px">· Umfassende Full-Service-Betreuung</li>
      <li style="margin-bottom:3px">· Nahtloser Integration in Ihre kaufmännischen<br>Prozesse</li>
      <li>· Vielseitigen Abrechnungsmöglichkeiten</li>
    </ul>
  </div>

  <div class="thumb" role="img" aria-label="Ladestecker an einer Wandbox mit gelbem Kabel, im Hintergrund eine Frau mit Tasche"
       style="left:314px;top:378px;width:108px;height:107px;background:linear-gradient(135deg,#8a8680 0%,#c9c2b6 55%,#d9c96a 100%)"></div>
  <div class="thumb" role="img" aria-label="Reihe von Ladestelen auf einem Parkplatz vor Bäumen"
       style="left:314px;top:490px;width:108px;height:108px;background:linear-gradient(180deg,#8c9a6a 0%,#c9a96a 45%,#6d6a66 100%)"></div>
  <div class="abs" style="left:431px;top:378px;width:53px;height:220px;background:linear-gradient(180deg,#e0359a 0%,#9e5bb3 100%)"></div>

  <div class="contact abs" style="left:22px;top:617px;width:220px">
    <h4>Kontaktieren Sie uns</h4>
    <p>Erfahren Sie mehr über vornix-tech<br>und wie wir Ihre Abrechnungsanforderungen<br>erfüllen können.</p>
  </div>
  <div class="abs" style="left:252px;top:616px;width:1.5px;height:56px;background:var(--band)"></div>
  <div class="contact abs" style="left:280px;top:617px;width:200px">
    <h4>für eine kostenlose Beratung:</h4>
    <p>Telefon: +49 (0) 9876 543 210<br>E-Mail: info@vornix-tech.de<br>Web: www.vornix-tech.de</p>
  </div>
</section>

<section class="page page--back">
  <div class="brand">vornix-tech.de</div>

  <div class="band" style="top:125px;height:134px"></div>
  <div class="photo" role="img" aria-label="Silbernes Elektro-SUV an einer schwarzen Schnellladesäule"
       style="left:218px;top:30px;width:266px;height:206px;border-radius:6px 0 0 6px;background:linear-gradient(160deg,#f1f1f3 0%,#cfd1d6 55%,#3a3b40 100%)"></div>
  <h1 class="title" style="top:155px;font-size:40px;line-height:37px">VORNIX-TECH<br>PROFESSIONAL</h1>
  <p class="band-sub" style="top:236px;font-size:10.5px">die Funktionen im Überblick</p>

  <div class="feature" style="left:9px">
    <div class="icon-box">
      <svg width="62" height="24" viewBox="0 0 62 24" aria-hidden="true" fill="#222">
        <rect x="1" y="9" width="16" height="8" rx="2"/><rect x="4" y="5" width="10" height="6" rx="2"/>
        <rect x="45" y="9" width="16" height="8" rx="2"/><rect x="48" y="5" width="10" height="6" rx="2"/>
        <rect x="18" y="8" width="26" height="11" rx="3"/><rect x="23" y="2" width="16" height="8" rx="3"/>
        <circle cx="24" cy="20" r="3"/><circle cx="38" cy="20" r="3"/>
      </svg>
    </div>
    <span>Fuhrpark,<br>Dienstwagen</span>
  </div>
  <div class="feature" style="left:129px">
    <div class="icon-box">
      <svg width="52" height="34" viewBox="0 0 52 34" aria-hidden="true" fill="#111">
        <circle cx="10" cy="7" r="5"/><path d="M1 22c0-6 4-9 9-9s9 3 9 9z"/>
        <circle cx="42" cy="7" r="5"/><path d="M33 22c0-6 4-9 9-9s9 3 9 9z"/>
        <circle cx="26" cy="13" r="6"/><path d="M15 33c0-7 5-11 11-11s11 4 11 11z"/>
      </svg>
    </div>
    <span>Mitarbeiter<br>Privatfahrzeuge</span>
  </div>
  <div class="feature" style="left:250px">
    <div class="icon-box">
      <svg width="44" height="52" viewBox="0 0 44 52" aria-hidden="true" fill="#111">
        <circle cx="8" cy="6" r="4"/><circle cx="22" cy="6" r="4"/><circle cx="36" cy="6" r="4"/>
        <circle cx="14" cy="18" r="4"/><circle cx="30" cy="18" r="4"/>
        <circle cx="22" cy="30" r="4"/>
        <rect x="2" y="11" width="12" height="14" rx="4"/><rect x="30" y="11" width="12" height="14" rx="4"/>
        <rect x="8" y="23" width="12" height="16" rx="4"/><rect x="24" y="23" width="12" height="16" rx="4"/>
        <rect x="16" y="35" width="12" height="16" rx="4"/>
      </svg>
    </div>
    <span>Kunden und<br>Gäste</span>
  </div>
  <div class="feature" style="left:370px">
    <div class="icon-box">
      <svg width="48" height="40" viewBox="0 0 48 40" aria-hidden="true" fill="#111">
        <rect x="8" y="2" width="12" height="14"/><rect x="2" y="16" width="12" height="24"/>
        <rect x="16" y="20" width="12" height="20"/><rect x="32" y="4" width="14" height="36"/>
      </svg>
    </div>
    <span>Vermieter,<br>Eigentümer</span>
  </div>

  <h2 class="section-head">Verrechnung von Ladevorgängen für:</h2>

  <div class="panel detail" style="left:0;top:420px;width:370px;height:246px;padding:10px 8px 0 21px">
    <h3>Full-Service-Betreuung für sorgenfreies Management</h3>
    <p>vornix-tech übernimmt auf Wunsch alle organisatorischen Belange bei<br>der Verwaltung Ihrer Lade-Infrastruktur, einschließlich:</p>
    <ul>
      <li>Monitoring</li>
      <li>Support</li>
      <li>User-Onboarding und -Support</li>
      <li>Handling von Zugangskarten</li>
      <li>Integration von firmeninternen Zugangstoken</li>
    </ul>
    <h3 style="margin-top:6px">Perfekte Integration in kaufmännische Prozesse</h3>
    <p>vornix-tech fügt sich nahtlos in die kaufmännischen Strukturen moderner<br>Unternehmen ein und bietet:</p>
    <ul>
      <li>Erweitertes Reporting</li>
      <li>Aufschlüsselung und Tarifierung nach Nutzergruppe</li>
      <li>Unterstützung unternehmensinterner Abrechnung und Verrechnung<br><span class="indent">und/oder Zahlungseinzug durch vornix-tech</span></li>
      <li>Schnittstellen zu Buchhaltung und Lohnbuchhaltung</li>
      <li>Bedarfsgerechte Anpassbarkeit</li>
    </ul>
  </div>
  <div class="photo" role="img" aria-label="Ladestecker in Nahaufnahme mit violett-pinkem Lichtschein"
       style="left:378px;top:420px;width:106px;height:246px;background:linear-gradient(180deg,#5a3fae 0%,#b04fb8 50%,#3a2f8a 100%)"></div>
</section>

</body>
</html>
```